Business Card Design Project

I need a new business card design for my building/development company: Kestrel Ridge Builders.

We specialise in small sub-divisions, multi-story developments and new house builds.
We handle the whole process from concept stage right throught to a fully developed property.
Updates

Target Market(s)

people looking to develop their property and need help. New property buyers

Industry/Entity Type

House

Requirements
Must have
• My logo on both sides:
Side 1: Logo taking up whole side as per old card but with a color/style change.

Side 2: Contact page: include logo but the rest just surprise me!

All contact details will be: (and need to be changable for each employee) I'll inform you of specifics before printing.

Name Surname
Position ie. Managing director
M: insert mobile
E: insert email
P.O. Box 518, Ashwell, Vic, 3094
www.kestrelridgebuilders.com.au

Nice to have
• Colors i'd like: (not necessarily all but this is the basic idea)

Black, blue, grey, silver, white

```html
<!DOCTYPE html>
<html lang="en">
<head>
<meta charset="utf-8">
<title>Kestrel Ridge Builders — Business Card</title>
<link rel="stylesheet" href="https://fonts.googleapis.com/css2?family=Source+Sans+3:wght@400;600;700&display=swap">
<style>
  :root {
    --page-bg: #e4e4e4;
    --blue-deep: #0b63ad;
    --blue-mid: #1479c6;
    --blue-light: #2a9be0;
    --brand-blue: #1b8fd8;
    --ink: #1f1f1f;
    --white: #ffffff;
    --silver: #b3b3b3;
    --silver-dark: #8a8a8a;
  }
  * { box-sizing: border-box; margin: 0; padding: 0; }
  html, body {
    width: 1200px; height: 900px; overflow: hidden;
    background: var(--page-bg);
    font-family: "Source Sans 3", "Myriad Pro", sans-serif;
  }
  .canvas { position: relative; width: 1200px; height: 900px; }

  .card {
    position: absolute; left: 292px; width: 616px; height: 377px; overflow: hidden;
  }
  .card--front {
    top: 40px;
    background: radial-gradient(ellipse 70% 80% at 28% 42%, var(--blue-light) 0%, var(--blue-mid) 45%, var(--blue-deep) 100%);
  }
  .card--back { top: 481px; background: var(--white); }

  /* Front */
  .front-brand__mark {
    position: absolute; left: 112px; top: 92px; width: 96px; height: 96px;
    background: var(--white);
  }
  .front-brand { position: absolute; left: 45px; top: 203px; }
  .front-brand__name {
    font-weight: 700; font-size: 33px; line-height: 1; color: var(--white); letter-spacing: -0.5px;
  }
  .front-brand__tagline {
    font-weight: 600; font-size: 16px; color: var(--white); margin-top: 3px; letter-spacing: 0.2px;
  }
  .front-url {
    position: absolute; left: 57px; top: 270px;
    font-size: 21px; color: var(--white);
  }

  /* Back */
  .back-brand { position: absolute; left: 52px; top: 62px; display: flex; align-items: center; gap: 18px; }
  .back-brand__mark { width: 64px; height: 64px; background: var(--brand-blue); }
  .back-brand__name {
    font-weight: 700; font-size: 40px; line-height: 1; color: var(--brand-blue); letter-spacing: -0.5px;
  }
  .back-brand__tagline {
    font-weight: 600; font-size: 17px; color: var(--ink); margin-top: 2px;
  }
  .back-wave { position: absolute; left: 0; top: 0; width: 616px; height: 377px; }

  .person { position: absolute; right: 372px; top: 270px; text-align: right; color: var(--white); }
  .person__name { font-weight: 700; font-size: 21px; line-height: 1.1; }
  .person__role { font-size: 16px; line-height: 1.3; }

  .divider {
    position: absolute; left: 283px; top: 255px; width: 2px; height: 87px; background: var(--white);
  }
  .contact { position: absolute; left: 308px; top: 256px; list-style: none; color: var(--white); font-size: 16px; }
  .contact li { display: flex; align-items: center; height: 20px; }
  .contact__icon { width: 14px; height: 14px; margin-left: -4px; margin-right: 8px; flex: none; }
</style>
</head>
<body>
<main class="canvas">

  <section class="card card--front" aria-label="Business card front">
    <div class="front-brand__mark"></div>
    <div class="front-brand">
      <div class="front-brand__name">Kestrel Ridge Builders</div>
      <div class="front-brand__tagline">renovation-construction-development</div>
    </div>
    <div class="front-url">www.kestrelridgebuilders.com.au</div>
  </section>

  <section class="card card--back" aria-label="Business card back">
    <svg class="back-wave" viewBox="0 0 616 377" aria-hidden="true">
      <defs>
        <linearGradient id="band-silver" x1="0" x2="1">
          <stop offset="0" stop-color="#d6d6d6"/>
          <stop offset="0.5" stop-color="#8a8a8a"/>
          <stop offset="1" stop-color="#6f6f6f"/>
        </linearGradient>
        <linearGradient id="band-blue" x1="0" y1="0" x2="1" y2="1">
          <stop offset="0" stop-color="#1a86d2"/>
          <stop offset="1" stop-color="#0b5fa8"/>
        </linearGradient>
      </defs>
      <path d="M0 214 C120 240 250 226 370 196 C470 172 560 168 616 176 L616 377 L0 377 Z" fill="url(#band-silver)"/>
      <path d="M0 226 C120 252 250 236 370 208 C470 186 560 182 616 190 L616 377 L0 377 Z" fill="url(#band-blue)"/>
    </svg>

    <div class="back-brand">
      <div class="back-brand__mark"></div>
      <div>
        <div class="back-brand__name">Kestrel Ridge Builders</div>
        <div class="back-brand__tagline">renovation-construction-development</div>
      </div>
    </div>

    <div class="person">
      <div class="person__name">Daniel Marsh</div>
      <div class="person__role">Managing Director</div>
    </div>

    <div class="divider"></div>

    <ul class="contact">
      <li>P.O. Box 518, Ashwell, Vic, 3094</li>
      <li>
        <svg class="contact__icon" viewBox="0 0 14 14" aria-hidden="true"><rect x="4" y="1" width="6" height="12" rx="1.2" fill="none" stroke="#fff" stroke-width="1.4"/><rect x="5.5" y="3" width="3" height="5" fill="#fff"/></svg>
        0412 555 274
      </li>
      <li>
        <svg class="contact__icon" viewBox="0 0 14 14" aria-hidden="true"><rect x="1" y="3" width="12" height="8" fill="#fff"/><path d="M1 3 L7 8 L13 3" fill="none" stroke="#1479c6" stroke-width="1.2"/></svg>
        daniel@kestrelridgebuilders.com.au
      </li>
      <li>
        <svg class="contact__icon" viewBox="0 0 14 14" aria-hidden="true"><circle cx="7" cy="7" r="5.8" fill="#fff"/><path d="M1.5 7 H12.5 M7 1.2 V12.8 M7 1.2 C4 4 4 10 7 12.8 M7 1.2 C10 4 10 10 7 12.8" fill="none" stroke="#1479c6" stroke-width="0.9"/></svg>
        www.kestrelridgebuilders.com.au
      </li>
    </ul>
  </section>

</main>
</body>
</html>
```